Banner for real estate email blast

I need a banner created that will be used in a commercial real estate broadcast email headed. The banner size should be 800x129 pixels and in a JPG format. I will include our company logo and samples of some other company documents.
The banner MUST include (1) the company name, Holloway-Brisk Real Estate and (2) the following contact information:
472 Tindale Orchard Rd
Fayetteville, NC 28917
(910) 555-0143
www.HollowayBriskRE.example
Target Market(s)
Real estate agents.
Industry/Entity Type
Real Estate
Requirements
Must have
- 1. Company name
- 2. Contact info to include address, phone number, web address
- 3. Use the same green colors as in our other attached documents.
- 4. MUST be 800x129 pixels
Should not have
- Any other text other than what is mentioned in the "Must Haves"

```html
<!DOCTYPE html>
<html lang="en">
<head>
<meta charset="utf-8">
<title>Holloway-Brisk Real Estate – Email Banner</title>
<link rel="stylesheet" href="https://fonts.googleapis.com/css2?family=Crimson+Text:wght@400;700&display=swap">
<style>
  :root {
    --brand-green: #1c6b3b;
    --brand-green-light: #2a7a4a;
    --ink-white: #ffffff;
  }
  html, body {
    margin: 0;
    padding: 0;
    width: 1200px;
    height: 194px;
    overflow: hidden;
  }
  .banner {
    position: relative;
    width: 1200px;
    height: 194px;
    background: var(--brand-green);
    color: var(--ink-white);
    font-family: "Crimson Text", Georgia, serif;
    overflow: hidden;
  }
  .banner__flourish {
    position: absolute;
    left: 690px;
    top: 0;
    width: 380px;
    height: 194px;
    background: radial-gradient(ellipse at 55% 45%, var(--brand-green-light) 0%, rgba(42,122,74,0.45) 45%, rgba(28,107,59,0) 75%);
  }
  .banner__mark {
    position: absolute;
    left: 28px;
    top: 18px;
    width: 156px;
    height: 156px;
  }
  .banner__name {
    position: absolute;
    left: 214px;
    top: 22px;
    margin: 0;
    font-size: 64px;
    font-weight: 400;
    line-height: 1;
    letter-spacing: 0.5px;
    white-space: nowrap;
  }
  .banner__address {
    position: absolute;
    left: 218px;
    top: 104px;
    margin: 0;
    font-style: normal;
    font-size: 22px;
    line-height: 33px;
  }
  .banner__contact {
    position: absolute;
    left: 848px;
    top: 58px;
    margin: 0;
  }
  .banner__phone {
    display: block;
    font-size: 37px;
    font-weight: 700;
    line-height: 1;
  }
  .banner__web {
    display: block;
    margin-top: 6px;
    font-size: 20px;
    line-height: 1;
  }
</style>
</head>
<body>
  <header class="banner">
    <div class="banner__flourish" role="img" aria-label="Faint leafy scroll ornament in lighter green"></div>

    <svg class="banner__mark" viewBox="0 0 156 156" aria-hidden="true">
      <circle cx="78" cy="78" r="76" fill="var(--ink-white)"/>
    </svg>

    <h1 class="banner__name">Holloway Brisk</h1>

    <address class="banner__address">
      472 Tindale Orchard Rd<br>
      Fayetteville, NC 28917
    </address>

    <p class="banner__contact">
      <span class="banner__phone">(910) 555-0143</span>
      <span class="banner__web">www.HollowayBriskRE.example</span>
    </p>
  </header>
</body>
</html>
```